Building Referrer Relationships Booklet

4 page A4 booklet to give to potential professional referrers to establish a collaborative relationship.Needs to be bright, vibrant, colourful, friendly, inviting, in keeping with The Wren Clinic colours.
Want to provide potential referrer partners a great reason to choose to collaborate with us. They need to know who we are, what makes us different/appealing, and who we are looking for to connect with.
The final product should communicate high performance and connectedness.

Target Market(s)

professional medical allied health and fitness practitioners

Industry/Entity Type

Health

Requirements
Must have
• energetic, vibrant, engaging, inviting, images

```html
<!DOCTYPE html>
<html lang="en">
<head>
<meta charset="utf-8">
<title>The Wren Clinic – Referral Partnerships Booklet</title>
<link href="https://fonts.googleapis.com/css2?family=Open+Sans:wght@400;600;700&display=swap" rel="stylesheet">
<style>
:root{
  --orange:#f26f21;
  --blue:#1d4fa3;
  --navy:#0d2d6b;
  --deep:#0a2563;
  --ink:#333;
  --paper:#f4f4f4;
  --stage:#e6e6e6;
  --photo-warm:#9c7a62;
  --photo-grass:#6f8a4a;
}
*{box-sizing:border-box;margin:0;padding:0}
html,body{width:926px;height:1200px;overflow:hidden;background:var(--stage);font-family:"Open Sans",Arial,sans-serif;color:var(--ink)}
.spread{position:absolute;left:82px;width:754px;height:533px;display:flex;box-shadow:0 6px 12px rgba(0,0,0,.18)}
.spread--outer{top:35px}
.spread--inner{top:622px}
.page{position:relative;width:377px;height:533px;background:var(--paper);overflow:hidden}
.page svg.bg{position:absolute;left:0;top:0}
.abs{position:absolute}
ul{list-style:none}

/* outer back page */
.achieve{left:0;top:0;width:377px;height:120px;background:var(--orange);color:#fff;padding:14px 15px;display:flex;gap:16px}
.achieve h3{font-size:7px;font-weight:400;margin-bottom:9px}
.achieve li{font-size:5.6px;line-height:8.8px}
.achieve li::before{content:"• "}
.achieve .col{width:170px}
.partners-title{top:133px;width:100%;text-align:center;color:var(--orange);font-size:6.6px}
.partners{left:17px;top:150px;width:350px}
.partners li{margin-bottom:5px}
.partners .role{font-size:7px;color:var(--blue);display:flex;align-items:center;gap:5px}
.partners li:nth-child(even) .role{color:var(--orange)}
.partners .role i{width:7px;height:7px;border:1px solid currentColor;border-radius:50%;display:inline-block}
.partners .note{font-size:5.8px;line-height:8px;padding-left:12px}
.partners .note::before{content:"• "}
.badges{top:436px;left:50px;display:flex;gap:14px;align-items:center}
.badges span{display:block;width:34px;height:12px;background:#c9ccd6;border-radius:2px}
.btn{left:113px;top:462px;width:142px;height:19px;border-radius:10px;background:#eef0f5;color:var(--blue);font-weight:600;font-size:11px;text-align:center;line-height:19px}
.address{top:492px;width:100%;text-align:center;color:#fff;font-size:8.4px}
.footer{left:0;top:503px;width:100%;height:21px;background:var(--orange);color:#fff;font-size:8.2px;display:flex;align-items:center;justify-content:space-around;padding:0 6px}
.footer span{display:flex;align-items:center;gap:4px}
.footer svg{width:8px;height:8px}
.base{left:0;top:524px;width:100%;height:9px;background:var(--navy)}

/* outer cover */
.cover-title{top:26px;width:100%;text-align:center;color:var(--blue);font-weight:700;font-size:15.5px;letter-spacing:.3px}
.cover-sub{top:53px;width:100%;text-align:center;color:#444;font-size:15px;letter-spacing:.6px}
.brand-mark{left:165px;top:405px;width:48px;height:48px;border:1px solid #fff;border-radius:50%}
.brand{top:458px;width:100%;text-align:center;color:#fff;font-size:9px}
.tagline{top:472px;width:100%;text-align:center;color:#fff;font-size:8.8px;line-height:15px}

/* inner left */
.values{left:14px;top:20px;font-size:10.3px;color:#fff;letter-spacing:.3px}
.values b{font-weight:400}
.values .o{color:var(--orange)}
.values .dot{color:var(--orange);margin:0 5px}
.value-list{left:14px;top:42px;width:355px;color:#fff;font-size:6.5px;line-height:13.3px}
.value-list em{font-style:normal;color:var(--orange)}
.value-list li{padding-left:9px;position:relative}
.value-list li::before{content:"";position:absolute;left:0;top:4px;width:5px;height:5px;border:1px solid var(--orange);border-radius:50%}
.way-head{right:6px;top:236px;color:var(--orange);font-size:7px}
.intro{left:15px;top:264px;color:var(--blue);font-size:7px}
.loved-title{left:17px;top:300px;color:var(--orange);font-size:7px;line-height:10px}
.loved-rule{left:17px;top:332px;width:62px;height:1px;background:var(--orange)}
.loved{left:14px;top:350px;width:170px}
.loved li{display:flex;gap:6px;margin-bottom:14px}
.loved .n{color:var(--orange);font-size:15px;line-height:15px}
.loved .t{font-size:6.4px}
.loved .t small{display:block;font-size:4.6px}
.divider{left:188px;top:298px;width:1px;height:140px;background:#ddd}
.way-text-title{left:13px;top:446px;color:var(--orange);font-size:7px}
.way-text{left:15px;top:458px;width:248px;font-size:6.5px;line-height:9.5px;text-align:justify;width:248px}
.team-title{left:204px;top:300px;color:var(--orange);font-size:7px}
.team{left:194px;top:316px;width:180px;display:grid;grid-template-columns:repeat(3,58px);row-gap:8px}
.member{text-align:center}
.member .face{width:48px;height:48px;margin:0 auto 4px;border-radius:50%;border:2px solid #ddd;background:linear-gradient(#e9e9e9,#c9c2bb)}
.member b{display:block;color:var(--blue);font-size:5px;font-weight:600}
.member small{display:block;font-size:4.2px;color:#555}
.strip{left:0;top:523px;width:100%;height:10px;background:var(--blue)}

/* inner right */
.photo-team{left:0;top:0;width:377px;height:175px;background:linear-gradient(180deg,#7fa0c8 0%,var(--photo-grass) 30%,#3a8f7a 55%,#274f63 100%)}
.circle-img{border-radius:50%;border:4px solid #fff}
.cw-title{left:19px;top:175px;color:var(--orange);font-size:7px}
.sub{color:var(--blue);font-size:7px;font-weight:600}
.grp{left:16px;display:flex;gap:14px;align-items:flex-start}
.grp .icon{width:26px;height:26px;border-radius:50%;background:radial-gradient(circle at 40% 35%,#3d78cf,var(--blue))}
.grp ul{font-size:6.8px;line-height:8.8px}
.grp li::before{content:"• ";color:var(--orange)}
</style>
</head>
<body>

<!-- OUTER SPREAD -->
<section class="spread spread--outer">
  <article class="page page--back">
    <svg class="bg" width="377" height="533" viewBox="0 0 377 533">
      <path d="M0 420 C120 450 260 430 377 402 L377 533 L0 533Z" fill="#8fa5cf"/>
      <path d="M0 428 C120 456 260 438 377 410 L377 533 L0 533Z" fill="#1a4395"/>
    </svg>
    <div class="abs achieve">
      <div class="col">
        <h3>Our Team Achievements:</h3>
        <ul>
          <li>Director, Sports Care Alliance (SCA)</li>
          <li>Director, Southern Academy of Sports Podiatry (SASP).</li>
          <li>External Advisor, Westfield University Podiatry Unit</li>
          <li>BFMA Level 1 Barefoot Rehabilitation Instructor</li>
          <li>Lower Limb Manual Therapy trained</li>
          <li>Fascia Lines trained</li>
          <li>Class 3b Laser Certified</li>
        </ul>
      </div>
      <div class="col">
        <h3>Our Athlete Experience:</h3>
        <ul>
          <li>National Sports Academy (NSA)</li>
          <li>National Rugby Squad</li>
          <li>Harbour City Games</li>
          <li>Coastal World Triathlon Series</li>
          <li>Southern Regional Games</li>
          <li>Westside Tennis Cup</li>
        </ul>
      </div>
    </div>
    <p class="abs partners-title">REFERRAL PARTNERS REQUIRED:</p>
    <ul class="abs partners">
      <li><p class="role"><i></i>Massage therapists</p><p class="note">Deep tissue and remedial massage</p><p class="note">Therapeutic massage</p></li>
      <li><p class="role"><i></i>Fascial therapists</p><p class="note">Fascia line releases to reset the alignment of the whole body</p></li>
      <li><p class="role"><i></i>Physiotherapists</p><p class="note">Pain relief, protect and strengthen both lower limb and upper limb</p></li>
      <li><p class="role"><i></i>GP, Sports Physicians</p><p class="note">General health,diagnostics, treatment support, prescription medications</p><p class="note">Specialist referrals</p></li>
      <li><p class="role"><i></i>Osteopaths and chiropractors</p><p class="note">Mobilisation and manipulative therapy for the spinal column and limbs</p></li>
      <li><p class="role"><i></i>Dietician and nutritionists</p><p class="note">DEXA scan for bone density/lean mass/fat mass</p><p class="note">Optimising gut health and nutrition - You are what you eat!</p></li>
      <li><p class="role"><i></i>Psychologists/psychiatrists</p><p class="note">Sometimes our physical body cannot get better until we optimise a healthy mind</p></li>
      <li><p class="role"><i></i>Personal trainers, Pilates and yoga instructors</p><p class="note">Create awesome body strength, flexibility and resilience</p></li>
      <li><p class="role"><i></i>Surgeons</p><p class="note">When conservative methods are ineffective, surgical intervention works well.</p></li>
    </ul>
    <div class="abs badges" aria-label="Partner badges">
      <span></span><span></span><span></span><span></span><span></span><span></span>
    </div>
    <div class="abs btn">CONTACT US</div>
    <p class="abs address">Harbourside Centre 4 / 218 Coast Rd Bayview WA 6999</p>
    <div class="abs footer">
      <span><svg viewBox="0 0 10 10"><circle cx="5" cy="5" r="5" fill="#fff"/><rect x="2.5" y="3.3" width="5" height="3.4" fill="none" stroke="#f26f21" stroke-width=".8"/></svg>hello@wrenclinic.example</span>
      <span><svg viewBox="0 0 10 10"><circle cx="5" cy="5" r="5" fill="#fff"/><circle cx="5" cy="5" r="2" fill="#f26f21"/></svg>08 5550 1234</span>
      <span><svg viewBox="0 0 10 10"><circle cx="5" cy="5" r="4.4" fill="none" stroke="#fff"/><path d="M1 5h8M5 1v8" stroke="#fff" stroke-width=".7"/></svg>www.wrenclinic.example</span>
    </div>
    <div class="abs base"></div>
  </article>

  <article class="page page--cover">
    <svg class="bg" width="377" height="533" viewBox="0 0 377 533">
      <defs>
        <linearGradient id="hands" x1="0" y1="0" x2="1" y2="1">
          <stop offset="0" stop-color="#b58e72"/><stop offset=".5" stop-color="#7a5a48"/><stop offset="1" stop-color="#c9b7a8"/>
        </linearGradient>
        <linearGradient id="coverBlue" x1="0" y1="0" x2="0" y2="1">
          <stop offset="0" stop-color="#1b4aa0"/><stop offset="1" stop-color="#0d2d6b"/>
        </linearGradient>
      </defs>
      <path d="M0 98 C120 110 260 100 377 92 L377 382 L0 382Z" fill="#c9ccd4"/>
      <path role="img" aria-label="Photo: many hands stacked together in the centre" d="M0 102 C120 112 260 104 377 96 L377 380 C260 420 120 410 0 372Z" fill="url(#hands)"/>
      <path d="M0 372 C120 410 260 420 377 380 L377 533 L0 533Z" fill="#8fa5cf"/>
      <path d="M0 382 C120 416 260 428 377 392 L377 533 L0 533Z" fill="url(#coverBlue)"/>
    </svg>
    <h1 class="abs cover-title">REFERRAL PARTNERSHIPS</h1>
    <p class="abs cover-sub">Because Together We Achieve</p>
    <div class="abs brand-mark"></div>
    <p class="abs brand">thewrenclinic</p>
    <p class="abs tagline">We are here to help our clients get back on their feet<br>Let’s combine our skillsets so we can achieve even better results</p>
    <div class="abs footer">
      <span><svg viewBox="0 0 10 10"><circle cx="5" cy="5" r="5" fill="#fff"/><rect x="2.5" y="3.3" width="5" height="3.4" fill="none" stroke="#f26f21" stroke-width=".8"/></svg>hello@wrenclinic.example</span>
      <span><svg viewBox="0 0 10 10"><circle cx="5" cy="5" r="5" fill="#fff"/><circle cx="5" cy="5" r="2" fill="#f26f21"/></svg>08 5550 1234</span>
      <span><svg viewBox="0 0 10 10"><circle cx="5" cy="5" r="4.4" fill="none" stroke="#fff"/><path d="M1 5h8M5 1v8" stroke="#fff" stroke-width=".7"/></svg>www.wrenclinic.example</span>
    </div>
    <div class="abs base"></div>
  </article>
</section>

<!-- INNER SPREAD -->
<section class="spread spread--inner">
  <article class="page page--values">
    <svg class="bg" width="377" height="533" viewBox="0 0 377 533">
      <defs>
        <linearGradient id="valuesBlue" x1="0" y1="0" x2="1" y2="1">
          <stop offset="0" stop-color="#1f56b0"/><stop offset="1" stop-color="#0b2a69"/>
        </linearGradient>
      </defs>
      <path d="M0 0 H377 V222 C280 235 140 232 0 196Z" fill="url(#valuesBlue)"/>
      <path d="M0 196 C140 232 280 235 377 222 C280 240 140 245 0 212Z" fill="#fff" opacity=".85"/>
      <path d="M0 220 C130 258 250 250 310 232 C250 262 130 270 0 236Z" fill="#f26f21"/>
    </svg>
    <p class="abs values"><b class="o">COURAGE</b><span class="dot">•</span><b>INSPIRATION</b><span class="dot">•</span><b class="o">FUN</b><span class="dot">•</span><b>CREATIVE</b><span class="dot">•</span><b class="o">WOW</b><span class="dot">•</span><b>TEAM</b></p>
    <ul class="abs value-list">
      <li><em>COURAGE</em> gives us the strength and confidence to take risks and embrace challenges</li>
      <li><em>INSPIRATION</em> is our energy, our fuel for success, that life force that feeds us as we grow and develop.</li>
      <li><em>FUN</em> generates happiness, and we all function at our best when we are happy.</li>
      <li><em>CREATIVITY</em> sets us as an innovative leading-edge business.</li>
      <li><em>WOW</em> means being the very best we can be and realise our true potential.We are not your average business, our service is not average, and our people are not average.</li>
      <li><em>TEAM</em> and in particular high-performance team means we perform at our very best. Great teamwork creates unity and we accomplish much more than each of us alone.</li>
    </ul>
    <p class="abs way-head">THE WREN CLINIC WAY</p>
    <p class="abs intro">At The Wren Clinic, we are passionate about building strong postural foundations, from the feet up.</p>
    <p class="abs loved-title">The top 3 things our clients love about us<br>(and hopefully yours will too!):</p>
    <div class="abs loved-rule"></div>
    <ol class="abs loved">
      <li><span class="n">1</span><p class="t">Positive energy, enthusiasm and outcomes<small>NPS average score &gt;9 out of 10</small></p></li>
      <li><span class="n">2</span><p class="t">Trusted leader in the practice of podiatric medicine<small>established 1999, elite experience, latest high-tech equipment</small></p></li>
      <li><span class="n">3</span><p class="t">Focus is on strong feet, not just orthotics!<small>BFMA Barefoot Technology, Fascia Lines, Lower Limb Manual Therapy</small></p></li>
    </ol>
    <div class="abs divider"></div>
    <p class="abs way-text-title">THE WREN CLINIC WAY</p>
    <p class="abs way-text" style="width:170px">Our pathway to strengthen postural foundations, to create lasting changes for freedom of movement, and ultimately keep us going well beyond what we thought was possible (updated as research and tech changes).</p>
    <p class="abs team-title">OUR TEAM:</p>
    <div class="abs team">
      <div class="member"><div class="face" role="img" aria-label="Portrait photo of Dr Arun Pillai"></div><b>Dr Arun Pillai</b><small>(Principal Podiatrist)</small></div>
      <div class="member"><div class="face" role="img" aria-label="Portrait photo of Dr Kate Holloway"></div><b>Dr Kate Holloway</b><small>(Senior Podiatrist)</small></div>
      <div class="member"><div class="face" role="img" aria-label="Portrait photo of Dr Nina Castell"></div><b>Dr Nina Castell</b><small>(Podiatrist)</small></div>
      <div class="member"><div class="face" role="img" aria-label="Portrait photo of Dr Marcus Tan"></div><b>Dr Marcus Tan</b><small>(Podiatrist)</small></div>
      <div class="member"><div class="face" role="img" aria-label="Portrait photo of Leanne Bright"></div><b>Leanne Bright</b><small>(Practice Manager)</small></div>
      <div class="member"><div class="face" role="img" aria-label="Portrait photo of Jo Whitfield"></div><b>Jo Whitfield</b><small>(Front Office Administrator)</small></div>
    </div>
    <div class="abs strip"></div>
  </article>

  <article class="page page--way">
    <div class="abs photo-team" role="img" aria-label="Photo: group of masters runners in national singlets at a track event"></div>
    <svg class="bg" width="377" height="533" viewBox="0 0 377 533">
      <path d="M0 168 C120 150 250 110 377 118 L377 135 C250 130 120 170 0 182Z" fill="#f26f21" opacity=".9"/>
      <path d="M0 172 C120 158 250 122 377 128 L377 533 L0 533Z" fill="#f4f4f4"/>
    </svg>
    <div class="abs circle-img" role="img" aria-label="Illustration: anatomy of the foot" style="left:172px;top:106px;width:70px;height:70px;background:radial-gradient(#7a5a4a,#1a1a1a)"></div>
    <div class="abs circle-img" role="img" aria-label="Photo: podiatrist reviewing foot scans on a computer" style="left:264px;top:120px;width:100px;height:100px;background:linear-gradient(135deg,#e8e6e2,#9ba4b0)"></div>
    <p class="abs cw-title">THE WREN CLINIC WAY</p>
    <p class="abs sub" style="left:19px;top:189px">Fix Your Feet</p>
    <div class="abs grp" style="top:201px"><div class="icon" role="img" aria-label="Foot icon" style="margin-top:4px"></div><ul><li>Fix the pain</li><li>Provide analgesia</li><li>Reduce inflammation</li><li>Corn/callus/foreign body removal</li><li>Ingrown/thickened toenail repair and maintenance</li><li>Surgery</li></ul></div>
    <div class="abs grp" style="top:260px"><div class="icon" role="img" aria-label="Foot icon" style="margin-top:6px"></div><ul><li>Protect the feet (reduce damage, optimise stability, promote healing)</li><li>Reduce tissue damage</li><li>Optimise Foot Posture</li><li>Activate neuromuscular/reflexive balance stability</li><li>Promote tissue repair/cellular regeneration</li></ul></div>
    <div class="abs grp" style="top:311px"><div class="icon" role="img" aria-label="Foot icon" style="margin-top:2px"></div><ul><li>Strengthen the feet (increase strength and resilience)</li><li>Strengthen intrinsics</li><li>Connect foot strength to core strength</li><li>Stimulate neuromuscular strength</li></ul></div>
    <p class="abs sub" style="left:19px;top:354px">Biohack Your Body</p>
    <div class="abs grp" style="top:366px"><div class="icon" role="img" aria-label="Foot icon" style="margin-top:4px"></div><ul><li>Protect the whole body (stability)</li><li>Optimise Postural Alignment</li><li>Activate neuromuscular/reflexive balance stability</li><li>Customised corrective exercises</li><li>Improve cellular regeneration</li><li>Optimise nutrition/healthy gut</li><li>Optimise healthy mind</li></ul></div>
    <div class="abs grp" style="top:438px"><div class="icon" role="img" aria-label="Foot icon" style="margin-top:4px"></div><ul><li>Strengthen the whole body (strength, elasticity)</li><li>Strengthen the deep core (stabilisers)</li><li>Strengthen the outer core (mobilisers)</li><li>Increase fascial elasticity/strength</li><li>Increase functional strength</li><li>Increase endurance</li><li>Customised nutrition for specific performance</li></ul></div>
    <p class="abs sub" style="left:19px;top:505px">Repeat consistently</p>
    <div class="abs strip" style="background:var(--navy)"></div>
  </article>
</section>

</body>
</html>
```